Creative, fresh business card design for Brindlecrest Linings

We need a fresh, creative business card design for Brindlecrest Linings. We are the manufacturer of Brindlecrest Linings in Australia. Wall panels are 2400 x 1200mm panels made from MDF and feature 3D patterns on the face of the panel. The colours to be used are green, silver/grey and white RGB
Red 187
Green 207
Blue 65.

An idea is to possibly use a watermark of one of our designs as a background (like on the "Lattice" design on the left hand side of page 2 of our brochure).

Target Market(s)

Interior designers, architects, builders and home renovators

Industry/Entity Type

Business

Contact Information for Business Card

Details to go on the card are:
Our logo (attached),
Slogan: "Decorative panels for interiors and exteriors",
Contact name,
Position,
Mobile phone number,
Business address,
Business phone,
Business fax,
Website and
Email address.

I have attached a few images of our panels and our brochure for reference.

The colours of the business card should feature our logo colours which are: RGB
Red 187
Green 207
Blue 65

Requirements
Must have
• Very modern fonts and design. Some of the designs shown especially the "Weave" design which is a popular design.
Nice to have
• Creative but simple design. Very contemporary.
Should not have
• Anything ornate or old fashioned.

```html
<!DOCTYPE html>
<html lang="en">
<head>
<meta charset="utf-8">
<title>Brindlecrest Linings – Business Card</title>
<link rel="stylesheet" href="https://fonts.googleapis.com/css2?family=Open+Sans:wght@400;600&family=Courier+Prime&display=swap">
<style>
  :root {
    --page-bg: #e6e6e4;
    --card-white: #f7f6f3;
    --card-shade: #e9e7e2;
    --brand-green: rgb(187, 207, 65);
    --brand-green-deep: #9fb232;
    --silver: #b9bbbd;
    --text-grey: #4a4a4a;
    --rule-grey: #8a8a8a;
  }
  html, body {
    margin: 0;
    width: 1200px;
    height: 1000px;
    overflow: hidden;
    background: var(--page-bg);
  }
  .card {
    position: absolute;
    left: 100px;
    top: 220px;
    width: 1000px;
    height: 560px;
    overflow: hidden;
    box-shadow: 0 14px 30px rgba(0, 0, 0, 0.25);
  }
  .card__texture {
    position: absolute;
    inset: 0;
    background: linear-gradient(170deg, var(--card-white) 0%, var(--card-shade) 45%, var(--card-white) 70%, var(--card-shade) 100%);
  }
  .card__wave {
    position: absolute;
    left: 0;
    bottom: 0;
    width: 1000px;
    height: 560px;
  }
  .brand {
    position: absolute;
    left: 150px;
    top: 120px;
    width: 305px;
  }
  .brand__name {
    display: flex;
    align-items: center;
    gap: 9px;
    font-family: "Open Sans", sans-serif;
    font-weight: 600;
    font-size: 22px;
    color: var(--brand-green-deep);
    line-height: 1.1;
    white-space: nowrap;
  }
  .brand__mark {
    flex: none;
    width: 20px;
    height: 20px;
    background: var(--brand-green);
  }
  .brand__slogan {
    margin: 14px 0 0;
    font-family: "Courier Prime", monospace;
    font-size: 18px;
    line-height: 1.1;
    color: var(--text-grey);
  }
  .divider {
    position: absolute;
    left: 470px;
    top: 58px;
    width: 2px;
    height: 256px;
    background: var(--rule-grey);
  }
  .contact {
    position: absolute;
    left: 486px;
    top: 60px;
    margin: 0;
    padding: 0;
    list-style: none;
    font-family: "Open Sans", sans-serif;
    font-size: 19px;
    line-height: 29px;
    color: var(--text-grey);
    white-space: nowrap;
  }
  .contact__name {
    font-weight: 600;
    color: var(--brand-green-deep);
  }
  .contact__role {
    margin-bottom: 8px;
  }
</style>
</head>
<body>
  <main class="card">
    <div class="card__texture" role="img" aria-label="Soft white sculpted wave panel texture"></div>
    <svg class="card__wave" viewBox="0 0 1000 560" aria-hidden="true">
      <defs>
        <linearGradient id="waveFill" x1="0" y1="0" x2="0" y2="1">
          <stop offset="0" stop-color="rgb(187, 207, 65)"/>
          <stop offset="1" stop-color="#9fb232"/>
        </linearGradient>
      </defs>
      <path d="M0 372 C 70 364, 120 357, 170 359 C 380 364, 560 467, 770 464 C 880 462, 940 407, 1000 372 L1000 560 L0 560 Z" fill="#b9bbbd" transform="translate(0 -12)"/>
      <path d="M0 372 C 70 364, 120 357, 170 359 C 380 364, 560 467, 770 464 C 880 462, 940 407, 1000 372 L1000 560 L0 560 Z" fill="url(#waveFill)"/>
    </svg>

    <div class="brand">
      <div class="brand__name"><span class="brand__mark"></span>Brindlecrest Linings</div>
      <p class="brand__slogan">decorative panels for<br>interiors &amp; exteriors</p>
    </div>

    <div class="divider"></div>

    <ul class="contact">
      <li class="contact__name">Marcus Delaney</li>
      <li class="contact__role">Sales Manager</li>
      <li>Mobile: 0400 182 907</li>
      <li>Telephone: 02 9000 4182</li>
      <li>Business fax: 02 9000 4190</li>
      <li>14 Calder Lane, Ferncourt NSW 2170</li>
      <li>www.brindlecrestlinings.com.au</li>
      <li>sales@brindlecrestlinings.com.au</li>
    </ul>
  </main>
</body>
</html>
```